Need a "Coming Soon" Page

Hi There!

This should be a really simple project - I just need a coming soon page. I've attached my logo and an example of a coming soon page that I think is a good model.

It should appear as follows:

Harbor Lantern Homecare
Los Angeles' premier provider of LGBT culturally competent non medical home care for LGBT Seniors and people aging with HIV who need Assistance with Activities of Daily Living and/or companion care services.

Coming in Early 2015

Target Market(s)

Los Angeles based LGBT Seniors (50 years or older) and LA based people aging with HIV.

Industry/Entity Type

Medical

Font styles to use
Serif

Colors
00a98f
34b8a4

Requirements
Must have
• A place to capture the e-mail address of interested persons.

```html
<!DOCTYPE html>
<html lang="en">
<head>
<meta charset="utf-8">
<title>Harbor Lantern Homecare — Coming Soon</title>
<link rel="stylesheet" href="https://fonts.googleapis.com/css2?family=Lustria&family=Mulish:wght@300;400&display=swap">
<style>
  :root {
    --brand-green: #0b5a45;
    --footer-green: #076452;
    --alert-red: #d9292a;
    --ink: #1f2a28;
    --field-border: #d4d8d7;
    --card-white: rgba(255, 255, 255, 0.9);
    --photo-warm: #c9a57e;
    --photo-cream: #ede3d2;
    --photo-blue: #5f87b4;
    --photo-light-blue: #a9c3e3;
  }
  * { box-sizing: border-box; margin: 0; padding: 0; }
  html, body { width: 1200px; height: 673px; overflow: hidden; }
  body { position: relative; font-family: "Mulish", sans-serif; color: var(--ink); }

  .hero-photo {
    position: absolute; left: 0; top: 0; width: 1200px; height: 611px;
    background:
      radial-gradient(ellipse 260px 320px at 300px 260px, rgba(226,180,150,0.55), transparent 70%),
      radial-gradient(ellipse 260px 300px at 720px 260px, rgba(226,170,140,0.5), transparent 70%),
      linear-gradient(180deg, var(--photo-warm) 0%, var(--photo-cream) 22%, var(--photo-cream) 40%, transparent 60%),
      linear-gradient(90deg, var(--photo-blue) 0%, var(--photo-blue) 40%, var(--photo-light-blue) 55%, var(--photo-light-blue) 100%);
  }

  .signup-card {
    position: absolute; left: 169px; top: 180px; width: 862px; height: 363px;
    background: var(--card-white); border-radius: 3px;
  }

  .brand-name {
    position: absolute; left: 205px; top: 333px;
    display: flex; align-items: center; gap: 14px;
    font-family: "Lustria", serif; font-size: 33px; line-height: 1;
    color: var(--brand-green);
  }
  .brand-mark { width: 34px; height: 34px; border-radius: 50%; background: var(--brand-green); flex: none; }

  .launch-panel { position: absolute; left: 684px; top: 229px; width: 290px; }
  .launch-title {
    font-family: "Lustria", serif; font-weight: 400; font-size: 42px; line-height: 1;
    color: var(--brand-green); white-space: nowrap;
  }
  .launch-summary {
    margin-top: 14px; width: 278px; font-weight: 300; font-size: 11px; line-height: 19px;
    hyphens: auto;
  }

  .notify-form { position: absolute; left: 685px; top: 389px; width: 289px; }
  .email-field {
    display: flex; align-items: center; gap: 8px; height: 50px; padding: 0 10px;
    background: #fff; border: 1px solid var(--field-border); border-radius: 2px;
  }
  .email-field input {
    border: 0; outline: 0; flex: 1; min-width: 0; background: transparent;
    font-family: "Lustria", serif; font-size: 17px; color: #555;
  }
  .email-field input::placeholder { color: #555; }
  .notify-button {
    display: block; width: 100%; height: 42px; margin-top: 5px; border: 0; border-radius: 2px;
    background: var(--alert-red); color: #fff;
    font-family: "Lustria", serif; font-size: 17px; letter-spacing: 0.5px;
  }

  .site-footer {
    position: absolute; left: 0; top: 611px; width: 1200px; height: 62px;
    background: var(--footer-green); color: #fff;
    display: flex; align-items: center; justify-content: center;
    font-family: "Lustria", serif; font-size: 12px;
  }
</style>
</head>
<body>
  <div class="hero-photo" role="img" aria-label="Photo of two smiling senior men sitting together in a home kitchen"></div>

  <main class="signup-card"></main>

  <div class="brand-name"><span class="brand-mark"></span>Harbor Lantern Homecare</div>

  <section class="launch-panel" lang="en">
    <h1 class="launch-title">Coming Soon</h1>
    <p class="launch-summary">Los Angeles' premier provider of LGBT culturally competent non medical home care for LGBT Seniors and people aging with HIV who need Assistance with Activities of Daily Living</p>
  </section>

  <form class="notify-form">
    <label class="email-field">
      <svg width="20" height="14" viewBox="0 0 20 14" aria-hidden="true">
        <rect x="0.5" y="0.5" width="19" height="13" fill="none" stroke="#666"/>
        <path d="M0.5 0.5 L10 8 L19.5 0.5 M0.5 13.5 L7.5 6.5 M19.5 13.5 L12.5 6.5" fill="none" stroke="#666"/>
      </svg>
      <input type="email" placeholder="Enter Your Email Address" aria-label="Email address">
    </label>
    <button type="button" class="notify-button">NOTIFY ME</button>
  </form>

  <footer class="site-footer">© copyrights 2015 all rights reserved</footer>
</body>
</html>
```